Business Card Design Project

I have just chosen a logo and would now like this designed onto a business card for my hair salon. I would like it to be classy not to busy and have a wow factor when people look at them
Has to Include on card:
Logo Design
And business details below
Kellie-ann Drummond (owner)
0482 736 219
Rdw@vomblet.com.au
71 Willowmere Rise Corvin Cove
Logo is now attached please provide designs
Hair

```html
<!DOCTYPE html>
<html lang="en">
<head>
<meta charset="utf-8">
<title>Lumiere Hair Studio — Business Card</title>
<link rel="stylesheet" href="https://fonts.googleapis.com/css2?family=Cinzel:wght@500&family=Philosopher:ital,wght@1,700&family=Raleway:wght@300&family=Arimo&display=swap">
<style>
  :root {
    --backdrop: #d6d6d6;
    --lime: #b8ff00;
    --lime-glow: #f4ffd8;
    --ink: #0a0a0a;
    --white: #ffffff;
    --soft-white: #e8e8f4;
  }
  html, body {
    margin: 0;
    width: 1200px;
    height: 1000px;
    overflow: hidden;
    background: var(--backdrop);
  }
  .card {
    position: absolute;
    left: 70px;
    top: 195px;
    width: 1062px;
    height: 613px;
    overflow: hidden;
    background:
      radial-gradient(circle at 262px 368px, var(--lime-glow) 0, rgba(244,255,216,0.5) 90px, rgba(184,255,0,0) 260px),
      var(--lime);
  }
  .hair-art {
    position: absolute;
    left: 0;
    top: 0;
    width: 1062px;
    height: 613px;
  }
  .brand-name {
    position: absolute;
    left: 37px;
    top: 240px;
    margin: 0;
    font-family: "Cinzel", serif;
    font-weight: 500;
    color: var(--ink);
    line-height: 1;
  }
  .brand-name .line-main {
    display: block;
    font-size: 92px;
    letter-spacing: 1px;
  }
  .brand-name .line-sub {
    display: block;
    font-size: 64px;
    margin-top: 4px;
  }
  .owner {
    position: absolute;
    right: 35px;
    top: 52px;
    width: 400px;
    text-align: right;
  }
  .owner-role {
    position: absolute;
    left: 95px;
    top: 0;
    font-family: "Raleway", sans-serif;
    font-weight: 300;
    font-size: 21px;
    color: var(--soft-white);
  }
  .owner-name {
    margin: 30px 0 0;
    font-family: "Philosopher", sans-serif;
    font-style: italic;
    font-weight: 700;
    font-size: 40px;
    color: var(--white);
    line-height: 1;
  }
  .owner-phone {
    margin: 6px 0 0;
    font-family: "Raleway", sans-serif;
    font-weight: 300;
    font-size: 29px;
    letter-spacing: 2px;
    color: var(--soft-white);
  }
  .contact {
    position: absolute;
    left: 590px;
    top: 502px;
    margin: 0;
    padding: 0;
    list-style: none;
    font-family: "Arimo", sans-serif;
    font-size: 27px;
    color: var(--ink);
  }
  .contact li {
    display: flex;
    align-items: center;
    height: 36px;
  }
  .contact svg {
    width: 28px;
    height: 28px;
    margin-right: 13px;
  }
</style>
</head>
<body>
  <section class="card">
    <svg class="hair-art" viewBox="0 0 1062 613" role="img" aria-label="Flowing black hair illustration sweeping across the top right">
      <path fill="var(--ink)" d="M483,0 L1062,0 L1062,295 C1030,322 990,340 962,322 C935,302 905,356 852,350 C800,344 790,300 760,262 C730,228 700,276 660,270 C622,264 612,238 582,200 C556,170 520,176 492,150 C470,130 520,108 540,90 C556,72 520,60 472,72 C448,42 458,28 483,0 Z"/>
    </svg>

    <h1 class="brand-name">
      <span class="line-main">Lumiere</span>
      <span class="line-sub">Hair Studio</span>
    </h1>

    <div class="owner">
      <span class="owner-role">Owner</span>
      <p class="owner-name">Kellie-ann Drummond</p>
      <p class="owner-phone">0482 736 219</p>
    </div>

    <ul class="contact">
      <li>
        <svg viewBox="0 0 28 28" aria-hidden="true">
          <path d="M3,14 L14,4 L25,14" fill="none" stroke="var(--ink)" stroke-width="2.5"/>
          <rect x="7" y="13" width="14" height="11" fill="none" stroke="var(--ink)" stroke-width="2.5"/>
          <rect x="12" y="17" width="4" height="7" fill="var(--ink)"/>
        </svg>
        71 Willowmere Rise Corvin Cove
      </li>
      <li>
        <svg viewBox="0 0 28 28" aria-hidden="true">
          <circle cx="14" cy="14" r="12" fill="var(--ink)"/>
          <circle cx="14" cy="14" r="4" fill="none" stroke="var(--lime)" stroke-width="2.2"/>
          <path d="M18,11 L18,16 C18,19 22,19 22,14 A8,8 0 1 0 17,21" fill="none" stroke="var(--lime)" stroke-width="2.2"/>
        </svg>
        Rdw@vomblet.com.au
      </li>
    </ul>
  </section>
</body>
</html>
```